Bluefinch Painting needs a Website

We need a website built for a Painting company I own, we mainly do residential painting, but don't want to be limited to that.

Need to have estimate request form.
Need pic's of past projects

I like the look of the website for http://www.harborline-painters.example
& "Thistledown Property inspections"

My logo that was designed here on ArtHive on the front page

I would like one of the houses I downloaded as part of the background
of the front page.

Target Market(s)

Home owners

Industry/Entity Type

Painting

Number of Pages Required

1 page

Font styles to use
Serif

Requirements
Must have
• Estimate request form for home owners to fill out -
• Name:
• Phone Number:
• Address:
• E-mail:
• Painting project description:
• And my info to:
• My phone number: (555) 318-7764
• My web address bluefinchpainting.example
Nice to have
• My logo that was designed here on ArtHive

```html
<!DOCTYPE html>
<html lang="en">
<head>
<meta charset="utf-8">
<title>Bluefinch Painting</title>
<link rel="stylesheet" href="https://fonts.googleapis.com/css2?family=Roboto+Slab:wght@400;700&family=Open+Sans:wght@300;400;600&family=Noto+Serif:wght@400;700&display=swap">
<style>
  :root {
    --ink: #2b2b2b;
    --white: #ffffff;
    --brand-blue: #2f9ee0;
    --link-blue: #7fd0ff;
    --section-blue: #5ab4e0;
    --band-dark: #1b78bf;
    --band-light: #41b9ec;
    --button-blue: #0b8fdc;
    --footer-bg: #222222;
    --footer-text: #e6e6e6;
    --rule-light: rgba(255,255,255,0.55);
    --rule-grey: #e2e2e2;
    --social-grey: #c9c9c9;
  }
  * { box-sizing: border-box; margin: 0; padding: 0; }
  html, body { width: 1200px; height: 2276px; overflow: hidden; background: var(--white); }
  body { position: relative; font-family: "Noto Serif", Georgia, serif; color: var(--ink); }

  /* Header */
  .site-header { position: absolute; left: 0; top: 0; width: 1200px; height: 101px; background: var(--white); box-shadow: 0 2px 6px rgba(0,0,0,0.25); z-index: 2; }
  .brand { position: absolute; left: 161px; top: 30px; display: flex; align-items: center; gap: 12px; font-family: "Roboto Slab", Georgia, serif; font-weight: 700; font-size: 30px; color: var(--brand-blue); letter-spacing: 1px; }
  .brand-square { width: 34px; height: 34px; background: var(--brand-blue); }
  .social { position: absolute; display: flex; gap: 8px; }
  .social span { width: 21px; height: 21px; background: var(--social-grey); }
  .social span:first-child { background: #3b5a99; }
  .site-header .social { left: 763px; top: 26px; }
  .header-phone { position: absolute; left: 889px; top: 21px; font-family: "Open Sans", Arial, sans-serif; font-size: 22px; color: var(--brand-blue); }
  .main-nav { position: absolute; left: 657px; top: 65px; display: flex; font-size: 12px; letter-spacing: 0.5px; }
  .main-nav a { color: var(--ink); text-decoration: none; }
  .main-nav a:nth-child(1) { width: 86px; }
  .main-nav a:nth-child(2) { width: 104px; }
  .main-nav a:nth-child(3) { width: 109px; }

  /* Hero */
  .hero { position: absolute; left: 0; top: 101px; width: 1200px; height: 382px; background: linear-gradient(180deg, #5b7d6a 0%, #35434d 40%, #3f4a52 70%, #54704a 100%); }
  .hero-text { position: absolute; left: 285px; top: 166px; width: 630px; text-align: center; font-size: 20px; line-height: 28px; color: var(--white); text-shadow: 0 1px 3px rgba(0,0,0,0.6); }
  .hero-text a { color: var(--link-blue); font-weight: 700; text-decoration: underline; }

  /* Quote band */
  .quote-band { position: absolute; left: 0; top: 483px; width: 1200px; height: 101px; background: linear-gradient(90deg, var(--band-dark) 0%, #2a95d6 55%, var(--band-light) 100%); }
  .quote-band-brush { position: absolute; left: 805px; top: 0; width: 203px; height: 101px; background: linear-gradient(90deg, #2b8fd4, #50c2ef); z-index: 0; }
  .quote-band-title { position: absolute; left: 314px; top: 32px; z-index: 1; white-space: nowrap; font-family: "Roboto Slab", Georgia, serif; font-weight: 700; font-size: 28px; line-height: 36px; letter-spacing: 8px; color: var(--white); }

  /* Welcome + form */
  .intro { position: absolute; left: 0; top: 584px; width: 1200px; height: 470px; background: var(--section-blue); color: var(--white); }
  .section-title { font-family: "Roboto Slab", Georgia, serif; font-weight: 700; font-size: 24px; letter-spacing: 0.5px; }
  .welcome { position: absolute; left: 161px; top: 64px; width: 473px; }
  .welcome .section-title { padding-bottom: 10px; border-bottom: 1px solid var(--rule-light); }
  .welcome p { font-family: "Noto Serif", Georgia, serif; font-size: 11px; line-height: 18px; margin-top: 14px; }
  .welcome p + p { margin-top: 18px; }
  .quote-form { position: absolute; left: 671px; top: 64px; width: 368px; }
  .quote-form-head { display: flex; justify-content: space-between; align-items: baseline; margin-bottom: 15px; }
  .quote-form-head a { color: var(--white); font-size: 12px; font-weight: 700; text-decoration: none; }
  .field { display: block; width: 368px; height: 31px; margin-bottom: 6px; background: var(--white); border: 1px solid #d6e6ef; padding: 0 14px; font-family: "Open Sans", Arial, sans-serif; font-size: 12px; color: #888; line-height: 29px; }
  .field.description { height: 72px; line-height: 22px; padding-top: 4px; }
  .submit { display: block; width: 368px; height: 37px; margin-top: 8px; background: var(--button-blue); color: var(--white); border-bottom: 2px solid #0a75b6; font-weight: 700; font-size: 12px; text-align: center; line-height: 35px; }

  /* Projects */
  .projects { position: absolute; left: 161px; top: 1112px; width: 878px; }
  .projects .section-title { color: var(--ink); padding-bottom: 14px; border-bottom: 1px solid var(--rule-grey); }
  .gallery { position: absolute; left: 0; top: 68px; width: 878px; height: 812px; }
  .tile { position: absolute; }
  .t1 { left: 0; top: 0; width: 639px; height: 213px; background: linear-gradient(180deg, #9fb7cc, #7f858a 60%, #4f5d46); }
  .t2 { left: 639px; top: 0; width: 239px; height: 405px; background: linear-gradient(180deg, #b9d3ea, #8b8c82 45%, #6b6a64); }
  .t3 { left: 0; top: 213px; width: 299px; height: 192px; background: linear-gradient(180deg, #9cbdd6, #5e6e50 50%, #6b6d70); }
  .t4 { left: 299px; top: 213px; width: 340px; height: 192px; background: linear-gradient(180deg, #2c6fb7, #1f5797); }
  .t5 { left: 0; top: 405px; width: 239px; height: 407px; background: linear-gradient(180deg, #8fbde6, #a79f86 45%, #5b7a3c); }
  .t6 { left: 239px; top: 405px; width: 639px; height: 213px; background: linear-gradient(180deg, #6c7a5c, #3f4538 55%, #4c5a3c); }
  .t7 { left: 239px; top: 618px; width: 341px; height: 194px; background: linear-gradient(180deg, #7fb1e0, #6d7a68 50%, #5d5f61); }
  .t8 { left: 580px; top: 618px; width: 298px; height: 194px; background: linear-gradient(180deg, #8cc0ea, #948f7d 50%, #6a8540); }
  .tile-overlay { position: absolute; inset: 0; display: flex; flex-direction: column; align-items: center; justify-content: center; gap: 8px; color: var(--white); font-weight: 700; font-size: 12.5px; line-height: 17px; text-align: center; }

  /* Footer */
  .site-footer { position: absolute; left: 0; top: 2052px; width: 1200px; height: 224px; background: var(--footer-bg); color: var(--footer-text); }
  .footer-nav { position: absolute; left: 163px; top: 50px; list-style: none; font-size: 12px; line-height: 24px; }
  .footer-nav a { color: var(--footer-text); text-decoration: none; }
  .footer-nav .current a { color: var(--brand-blue); }
  .footer-contact { position: absolute; left: 380px; top: 52px; width: 300px; text-align: center; }
  .footer-contact-title { font-weight: 700; font-size: 14px; color: var(--white); }
  .footer-phone { font-family: "Open Sans", Arial, sans-serif; font-size: 27px; color: var(--brand-blue); margin-top: 4px; }
  .footer-web { font-size: 15px; margin-top: 2px; }
  .footer-brand { position: absolute; right: 161px; top: 55px; display: flex; align-items: center; gap: 12px; font-family: "Roboto Slab", Georgia, serif; font-weight: 700; font-size: 30px; color: var(--brand-blue); letter-spacing: 1px; }
  .footer-copy { position: absolute; right: 161px; top: 115px; font-size: 12px; color: var(--white); }
  .site-footer .social { right: 161px; top: 147px; }
  .site-footer .social span { background: #555; }
  .site-footer .social span:first-child { background: #3b5a99; }
</style>
</head>
<body>
  <header class="site-header">
    <div class="brand"><span class="brand-square"></span>Bluefinch Painting</div>
    <div class="social" aria-label="Social links"><span></span><span></span><span></span><span></span></div>
    <div class="header-phone">(555) 318-7764</div>
    <nav class="main-nav">
      <a href="#about">ABOUT</a>
      <a href="#services">SERVICES</a>
      <a href="#projects">PROJECTS</a>
      <a href="#quote">FREE QUOTE</a>
    </nav>
  </header>

  <section class="hero" role="img" aria-label="Photo of a dark grey two-storey house with a garage and green garden">
    <p class="hero-text">We offer Interior and Exterior House Painting throughout the USA. Get a <a href="#quote">Free Quote</a></p>
  </section>

  <section class="quote-band">
    <div class="quote-band-brush" role="img" aria-label="Illustration of a paint brush"></div>
    <div class="quote-band-title">GET A FREE QUOTE NOW!</div>
  </section>

  <section class="intro" id="about">
    <div class="welcome">
      <h2 class="section-title">WELCOME</h2>
      <p>We are a family owned painting crew serving home owners with careful preparation, clean lines and lasting finishes. Every project starts with a walk through, an honest estimate and a clear schedule. We protect floors, furniture and gardens, repair damaged siding and trim, and prime every surface before the first coat goes on. Our painters use premium paints chosen for your climate, and we clean up each day so your home stays livable while we work.</p>
      <p>From interior walls and ceilings to decks, fences and full exteriors, no job is too large or too small. Tell us about your project and we will help you pick colours, plan the work and keep it within budget.</p>
      <p>Request your free quote today and see why neighbours trust us with the homes they love.</p>
    </div>
    <form class="quote-form" id="quote">
      <div class="quote-form-head">
        <h2 class="section-title">FREE QUOTE</h2>
        <a href="#quote">Estimate Request Form &gt;</a>
      </div>
      <div class="field">Name *</div>
      <div class="field">Phone Number *</div>
      <div class="field">Address *</div>
      <div class="field">E-mail *</div>
      <div class="field description">Description...</div>
      <div class="submit">GET YOUR FREE QUOTE</div>
    </form>
  </section>

  <section class="projects" id="projects">
    <h2 class="section-title">OUR PREVIOUS PROJECTS</h2>
    <div class="gallery">
      <div class="tile t1" role="img" aria-label="Photo of a large grey house with tall windows"></div>
      <div class="tile t2" role="img" aria-label="Photo of a house entrance with a stone path and flowers"></div>
      <div class="tile t3" role="img" aria-label="Photo of work trucks and trailers parked by a house"></div>
      <div class="tile t4" role="img" aria-label="Photo of a painted house exterior under a blue overlay">
        <div class="tile-overlay">
          <svg width="24" height="24" viewBox="0 0 24 24" fill="none" stroke="#ffffff" stroke-width="2"><circle cx="10" cy="10" r="7"/><line x1="15" y1="15" x2="22" y2="22"/><line x1="10" y1="6.5" x2="10" y2="13.5"/><line x1="6.5" y1="10" x2="13.5" y2="10"/></svg>
          <span>EXTERIOR HOUSE<br>PAINTING</span>
        </div>
      </div>
      <div class="tile t5" role="img" aria-label="Photo of a beige house with a front lawn and flower beds"></div>
      <div class="tile t6" role="img" aria-label="Photo of a dark painted house with a garage and trees"></div>
      <div class="tile t7" role="img" aria-label="Photo of a pickup truck and work trailer in front of a house"></div>
      <div class="tile t8" role="img" aria-label="Photo of a tan house with pink flowering shrubs"></div>
    </div>
  </section>

  <footer class="site-footer">
    <ul class="footer-nav">
      <li class="current"><a href="#">HOME</a></li>
      <li><a href="#about">ABOUT</a></li>
      <li><a href="#services">SERVICES</a></li>
      <li><a href="#projects">PROJECTS</a></li>
      <li><a href="#quote">FREE QUOTE</a></li>
    </ul>
    <div class="footer-contact">
      <div class="footer-contact-title">CALL FOR A FREE QUOTE</div>
      <div class="footer-phone">(555) 318-7764</div>
      <div class="footer-web">bluefinchpainting.example</div>
    </div>
    <div class="footer-brand"><span class="brand-square"></span>Bluefinch Painting</div>
    <div class="footer-copy">© 2014 Bluefinch Painting. All Rights Reserved.</div>
    <div class="social" aria-label="Social links"><span></span><span></span><span></span><span></span></div>
  </footer>
</body>
</html>
```